Business Cards & Stationary for Broadcast Company

We are a satellite company launching a new exciting brand by the name of "Veloran". Veloran is a broadcasting solution provider that gives end-to-end solutions to TV channels and other content providers to deliver and distribute their content globally. Weather it be TV channels that need to be broadcasted in their local regions or internationally, or its collection of news from various locations, or even coverage of special sports or other events, we provide the technology and services to make that happen.
we need a design for business cards as our top priority but also require letterhead and envelope design as well.
Business card will include the following information
Name: Karim Yusof
Designation: General Manager
Mobile (M): +92 321 4718296
+971 50 2846193 (UAE)
Direct (D): +92 213 4609142
Office (O): +92 213 4602518-22
Fax (F): +92 213 4609142
Email (E): karim@veloran.biz
Website: www.veloran.biz

```html
<!DOCTYPE html>
<html lang="en">
<head>
<meta charset="utf-8">
<title>Veloran Business Card</title>
<link rel="stylesheet" href="https://fonts.googleapis.com/css2?family=Mulish:wght@400;700&display=swap">
<style>
  :root {
    --bg: #d9d9d7;
    --card-white: #ffffff;
    --card-black: #0b0b0b;
    --ink: #333333;
    --ink-soft: #555555;
    --muted-light: #8a8a8a;
    --accent-blue: #1a73c7;
    --stripe-navy: #1760a8;
    --stripe-sky: #1ea7e1;
    --stripe-green: #8cc63f;
    --stripe-red: #d7282f;
    --icon-red: #d7282f;
    --brand-mark: #1e6fb8;
  }
  * { box-sizing: border-box; margin: 0; padding: 0; }
  html, body { width: 1200px; height: 871px; overflow: hidden; }
  body {
    background: var(--bg);
    font-family: "Mulish", "Century Gothic", sans-serif;
    position: relative;
  }
  .card {
    position: absolute;
    left: 280px;
    width: 640px;
    height: 366px;
    overflow: hidden;
    box-shadow: 0 6px 18px rgba(0,0,0,0.18);
  }
  .card--back { top: 40px; background: var(--card-black); }
  .card--front { top: 446px; background: var(--card-white); }

  .back-brand {
    position: absolute;
    left: 0; right: 0; top: 140px;
    text-align: center;
    font-size: 44px;
    font-weight: 700;
    letter-spacing: 2px;
    color: #d6d6d6;
  }
  .back-web {
    position: absolute;
    left: 0; right: 0; top: 270px;
    text-align: center;
    font-size: 16px;
    letter-spacing: 1px;
    color: var(--muted-light);
  }

  .front-brand {
    position: absolute;
    left: 50px; top: 130px;
    display: flex; align-items: center; gap: 12px;
    font-size: 40px;
    font-weight: 700;
    letter-spacing: 1px;
    color: var(--brand-mark);
  }
  .front-brand .dot {
    width: 18px; height: 18px; border-radius: 50%;
    background: var(--brand-mark);
  }

  .person { position: absolute; left: 390px; top: 96px; }
  .person-name { font-size: 19px; font-weight: 700; color: var(--ink); }
  .person-title { font-size: 12px; color: var(--accent-blue); margin-top: 2px; }

  .contacts {
    position: absolute; left: 374px; top: 160px;
    list-style: none;
  }
  .contacts li {
    display: flex; align-items: center; gap: 14px;
    height: 22px;
    font-size: 13.5px;
    color: var(--ink-soft);
    letter-spacing: 0.5px;
  }
  .contacts svg { width: 12px; height: 12px; flex: none; }

  .stripe {
    position: absolute; left: 0; right: 0; bottom: 0; height: 10px;
    display: flex;
  }
  .stripe span { flex: 1; }
  .stripe .navy { background: var(--stripe-navy); }
  .stripe .sky { background: var(--stripe-sky); }
  .stripe .green { background: var(--stripe-green); }
  .stripe .red { background: var(--stripe-red); }
</style>
</head>
<body>
  <section class="card card--back">
    <div class="back-brand">VELORAN</div>
    <div class="back-web">www.veloran.biz</div>
  </section>

  <section class="card card--front">
    <div class="front-brand"><span class="dot"></span>VELORAN</div>

    <div class="person">
      <div class="person-name">Karim Yusof</div>
      <div class="person-title">General Manager</div>
    </div>

    <ul class="contacts">
      <li>
        <svg viewBox="0 0 12 12" aria-label="Mobile"><rect x="3" y="0.5" width="6" height="11" rx="1" fill="none" stroke="var(--icon-red)" stroke-width="1.2"/><line x1="5" y1="9.5" x2="7" y2="9.5" stroke="var(--icon-red)"/></svg>
        +92 321 4718296
      </li>
      <li>
        <svg viewBox="0 0 12 12" aria-label="Mobile"><rect x="3" y="0.5" width="6" height="11" rx="1" fill="none" stroke="var(--icon-red)" stroke-width="1.2"/><line x1="5" y1="9.5" x2="7" y2="9.5" stroke="var(--icon-red)"/></svg>
        +971 50 2846193 (UAE)
      </li>
      <li>
        <svg viewBox="0 0 12 12" aria-label="Direct"><path d="M1 4 Q6 0 11 4 L9.5 5.5 L8 4.5 L8 3.5 Q6 3 4 3.5 L4 4.5 L2.5 5.5 Z" fill="var(--icon-red)"/><rect x="2.5" y="6.5" width="7" height="5" rx="1" fill="var(--icon-red)"/></svg>
        +92 213 4609142
      </li>
      <li>
        <svg viewBox="0 0 12 12" aria-label="Office"><path d="M1 4 Q6 0 11 4 L9.5 5.5 L8 4.5 L8 3.5 Q6 3 4 3.5 L4 4.5 L2.5 5.5 Z" fill="var(--icon-red)"/><rect x="2.5" y="6.5" width="7" height="5" rx="1" fill="var(--icon-red)"/></svg>
        +92 213 4602518-22
      </li>
      <li>
        <svg viewBox="0 0 12 12" aria-label="Fax"><rect x="3" y="0.5" width="6" height="4" fill="none" stroke="var(--icon-red)"/><rect x="0.5" y="4.5" width="11" height="5" rx="1" fill="var(--icon-red)"/><rect x="3" y="8" width="6" height="3.5" fill="#fff" stroke="var(--icon-red)"/></svg>
        +92 213 4609142
      </li>
      <li>
        <svg viewBox="0 0 12 12" aria-label="Email"><rect x="0.5" y="2" width="11" height="8" fill="none" stroke="var(--icon-red)" stroke-width="1.2"/><path d="M0.5 2 L6 6.5 L11.5 2" fill="none" stroke="var(--icon-red)" stroke-width="1.2"/></svg>
        karim@veloran.biz
      </li>
    </ul>

    <div class="stripe"><span class="navy"></span><span class="sky"></span><span class="green"></span><span class="red"></span></div>
  </section>
</body>
</html>
```